Tea standup pouch labels

Dear designers,
I need a minimalistic and modern label for my loose tea stand-up pouches (100, 250 and 500gm packs). The label should cover 70-80% of the pouch face (front and rear both).
The label will be 2 part label - Front and Rear side labels.
The labels should have a green background (Pantone Green C) with Golden or White or black colour text. Please either use the Golden logo or black logo to see which looks good with Pantone Green C background.
I am also attaching the content file and a few other files (Assam tea logo) to be used in the label.
The Assam tea logo should be small at the bottom left or right side of the front side. The logo should be dominant on the front page (some of the designs I received have small logo and big "100% single estate tea" and "Assam logo" as big characters on the front page which is not what I am looking for.

The font style should note simple Times new roman or Arial. It should look modern and should be something matching to the logo sentence 'Freshest possible' but should also not be in italics. Please refer to files Font style reference front and back for the style of font. Also use the same box space design on the rear - Content should be in White background; the rectangular box edges should be rounded and the border should be in dual colour - Golden and white or in black and white depending on the logo colour used (golden or black).

For the Rear page - headings could be in Golden colour or black colour depending on the logo colour you choose to use and the text can be in white colour i.e. Option 1 - Headings in golden colour and text in white colour; Option 2 - Heading in Black colour and text in white colour or any other combination that looks good - designer to decide.

Please let me know if you need any further information.

thanks,
Toral

```html
<!DOCTYPE html>
<html lang="en">
<head>
<meta charset="utf-8">
<title>Leafora – Tea Pouch Front Label</title>
<link rel="stylesheet" href="https://fonts.googleapis.com/css2?family=Oswald:wght@300;500&display=swap">
<style>
  :root {
    --teal: #35b7a5;
    --teal-deep: #2fa894;
    --ink: #0b0b0b;
    --mint: #c2fbf4;
    --mint-soft: #e6fdfa;
    --paper: #ffffff;
  }
  * { margin: 0; padding: 0; box-sizing: border-box; }
  html, body { width: 860px; height: 1200px; overflow: hidden; background: var(--paper); }
  .label {
    position: relative;
    width: 860px;
    height: 1200px;
    font-family: "Oswald", "Arial Narrow", sans-serif;
  }
  .brand-panel {
    position: absolute; left: 0; top: 0;
    width: 860px; height: 730px;
    background: var(--teal);
  }
  .brand-mark {
    position: absolute; left: 0; top: 190px; width: 860px;
    display: flex; flex-direction: column; align-items: center;
  }
  .brand-dot {
    width: 128px; height: 128px;
    border: 6px solid var(--ink);
    border-radius: 50%;
  }
  .brand-name {
    margin-top: 110px;
    font-weight: 300;
    font-size: 118px;
    line-height: 1;
    letter-spacing: 14px;
    padding-left: 14px;
    color: var(--ink);
  }
  .tagline-art {
    position: absolute; left: 258px; top: 615px;
    width: 345px; height: 62px;
    background: var(--teal-deep);
    border-radius: 4px;
  }
  .claim-band {
    position: absolute; left: 0; top: 730px;
    width: 860px; height: 78px;
    background: var(--ink);
    display: flex; align-items: center; justify-content: center;
  }
  .claim {
    color: var(--mint);
    font-weight: 500;
    font-size: 46px;
    letter-spacing: 9px;
  }
  .pattern-field {
    position: absolute; left: 0; top: 808px;
    width: 860px; height: 375px;
    background: linear-gradient(180deg, var(--paper), var(--mint-soft));
  }
  .net-weight {
    position: absolute; left: 0; top: 1040px; width: 860px;
    text-align: center;
    color: var(--ink);
    font-weight: 500;
    font-size: 38px;
    line-height: 44px;
    letter-spacing: 2px;
  }
  .origin-badge {
    position: absolute; left: 694px; top: 1028px;
    width: 124px; height: 124px;
    border: 2px solid var(--ink);
    border-radius: 50%;
    background: var(--paper);
  }
  .base-strip {
    position: absolute; left: 0; top: 1183px;
    width: 860px; height: 17px;
    background: var(--teal);
  }
</style>
</head>
<body>
<main class="label">
  <section class="brand-panel">
    <div class="brand-mark">
      <div class="brand-dot"></div>
      <div class="brand-name">LEAFORA</div>
    </div>
    <div class="tagline-art" role="img" aria-label="Handwritten script tagline: freshest possible"></div>
  </section>

  <div class="claim-band">
    <p class="claim">100% Single Estate Tea</p>
  </div>

  <div class="pattern-field" role="img" aria-label="Repeating pattern of pale mint tea leaves"></div>

  <p class="net-weight">Net Wt.<br>250g/8.82oz</p>

  <div class="origin-badge" role="img" aria-label="Regional tea origin badge"></div>

  <div class="base-strip"></div>
</main>
</body>
</html>
```